| Pairlocket | ||
| "Lanternmade Insurance" (this tagline includes the mathmatic "squared" symbol-see logo #161 winner) | ||
| Use fonts in logo. However, we may provide other direction on fonts for Address/Phone Numbers, etc. | ||
Cutting-Edge Modern Bright & Fun-filled |
| Dana R. Whitlock, MBA | ||
| Agency Principal | ||
| To Be Determined | ||
| TBD | ||
| dana@trypairlocket.com | ||
| www.trypairlocket.com | ||
1. We will need business cards for 2 people, Dana Whitlock (info provided above) and Morgan Whitlock...info as follows: Morgan P. Whitlock, MBA Agency Principal morgan@trypairlocket.com cell: 555.204.7316 2. Designer has provided final files to Mark Studio Hive. #161 was selected as Winner. This design has multiple components, please note. 3. Our logo style and design is somewhat "Retro" and cool, hip. We are in the insurance industry but definitely want to achieve a different "non-standard" look and feel. 4. Read Logo Brief for more information about the style of the two (twin brothers) Agency Principals. |
We are thinking that the "bottle cap" portion of our logo along with the "Pairlocket" portion would look good on the back of the business card. The bottle cap portion taking up most of the back of the card. Would like various options for the back. |
Download project material |
| pairlocket_17707.pdf |
| 1_17708.ai |
| Oak_Cellar_Depot_Business_Card_1_17709.jpg Pairlocket - Bus Card - example card design. We would like to see a style similar to this. |
| Brisk_Kettle_Business_Card_Example_17710.jpg Pairlocket - Bus Card - example card design. We would like to see a style similar to this. |

```html
<!DOCTYPE html>
<html lang="en">
<head>
<meta charset="utf-8">
<title>Pairlocket Business Card</title>
<link rel="stylesheet" href="https://fonts.googleapis.com/css2?family=Open+Sans:wght@400;600;700&display=swap">
<style>
  :root {
    --stage: #ece9e4;
    --card: #ffffff;
    --green: #5aa63b;
    --blue: #1f6fa8;
    --ink: #4a4a4a;
    --muted: #8a8a8a;
    --cap: #9aa3ab;
    --cap-inner: #2e7fb8;
  }
  * { margin: 0; padding: 0; box-sizing: border-box; }
  html, body {
    width: 1200px; height: 541px; overflow: hidden;
    background: var(--stage);
    font-family: "Open Sans", Arial, sans-serif;
  }
  .stage { position: relative; width: 1200px; height: 541px; }
  .card {
    position: absolute; top: 140px;
    width: 508px; height: 286px;
    background: var(--card);
    border-radius: 18px;
    box-shadow: 0 4px 14px rgba(0,0,0,.12);
    overflow: hidden;
  }
  .card--front { left: 70px; }
  .card--back { left: 616px; }

  .brand { position: absolute; left: 36px; top: 34px; width: 200px; text-align: center; }
  .brand__dot {
    width: 70px; height: 70px; border-radius: 50%;
    background: var(--green); margin: 0 auto 10px;
  }
  .brand__name { font-size: 34px; font-weight: 700; color: var(--green); letter-spacing: -0.5px; line-height: 1; }
  .brand__tagline {
    font-size: 8.5px; font-weight: 600; color: var(--green);
    letter-spacing: 1.6px; text-transform: uppercase; margin-top: 4px;
  }

  .contact { position: absolute; left: 293px; top: 66px; list-style: none; }
  .contact li { font-size: 12px; color: var(--ink); line-height: 16px; }

  .person { position: absolute; left: 293px; top: 158px; }
  .person__name { font-size: 16px; font-weight: 600; color: var(--green); }
  .person__name small { font-size: 11px; color: var(--ink); font-weight: 400; }
  .person__role { font-size: 11.5px; color: var(--ink); margin-top: 10px; }

  .divider {
    position: absolute; left: 36px; right: 0; top: 185px; height: 3px;
    background: linear-gradient(90deg, var(--green) 0 62%, var(--blue) 62% 100%);
  }
  .address { position: absolute; left: 30px; top: 233px; font-size: 12px; color: var(--ink); }

  .back-mark {
    position: absolute; left: 62px; top: 82px; width: 124px; height: 124px;
  }
  .back-site {
    position: absolute; left: 232px; top: 135px;
    font-size: 12.5px; color: var(--ink);
  }
</style>
</head>
<body>
<main class="stage">
  <section class="card card--front" aria-label="Card front">
    <div class="brand">
      <div class="brand__dot"></div>
      <div class="brand__name">Pairlocket</div>
      <div class="brand__tagline">Lanternmade Insurance</div>
    </div>

    <ul class="contact">
      <li>T : 000.000.0000</li>
      <li>C : 555.318.0427</li>
      <li>F : 000.000.0000</li>
      <li>E : dana@trypairlocket.com</li>
      <li>W : www.trypairlocket.com</li>
    </ul>

    <div class="person">
      <div class="person__name">Dana R. Whitlock, <small>MBA</small></div>
      <div class="person__role">Agency Principal</div>
    </div>

    <div class="divider"></div>
    <p class="address">Post box 0000 city abc road country</p>
  </section>

  <section class="card card--back" aria-label="Card back">
    <svg class="back-mark" viewBox="0 0 124 124" aria-hidden="true">
      <circle cx="62" cy="62" r="60" fill="var(--cap)"/>
      <circle cx="62" cy="62" r="44" fill="var(--cap-inner)"/>
    </svg>
    <p class="back-site">www.trypairlocket.com</p>
  </section>
</main>
</body>
</html>
```